Create Premium Wine Label Design

We are premium wine exporters from Australia. We are looking to introduce new brand " The Velloran" - in red wine, White wine and Sparkling wine to international market.

The sample label design for red wine ( Shiraz) is attached.

This is our luxury brand. We need a stunning wine label designs for (front, back and neck) that should be mostly in GOLD colour and design should be really eye catching.

We have provided sample design for front, back and neck labels. However, we are looking forward to see a completely new improvised design.

LOGO attached.

Front Label Design Specification:

* We would like to see designs that are in Gold colour.
* Wine Bottle size is standard: 750ml; we assume the same design can be resizable to different bottle sizes.
* Our design should suit both black, white and sparkling wine bottles(sample attached)
* Use our logo in the design (see attached - label sample)
* Content for front label (see attached).
* Design should include all information specified in the sample

Back Label Design
* All contents in the sample should be used ( sample attached)
* LOGO attached.

Neck Label Design
* Sample of Neck label attached, please provide similar or your own design.
* LOGO attached.

Image Samples:
* Samples of label designs we like (see attached)
* Sample for gold color (see attached)
* For bottle shapes (see attached)
* Front, Back and Neck Label Samples (see attached)

Target Market(s)

International Wine Market

Font styles to use
Decorative
Script

Requirements
Must have
• Must have golden color on front and back label

```html
<!DOCTYPE html>
<html lang="en">
<head>
<meta charset="utf-8">
<title>Gilded Crest Shiraz – Front Label</title>
<link rel="stylesheet" href="https://fonts.googleapis.com/css2?family=Poiret+One&display=swap">
<style>
  :root {
    --page: #ffffff;
    --label-black: #050505;
    --gold-light: #f3d58a;
    --gold: #c99a45;
    --gold-deep: #7a5a22;
    --gold-muted: #6e5426;
    --ivory: #f7f4ee;
  }
  html, body {
    margin: 0;
    padding: 0;
    width: 1200px;
    height: 1200px;
    overflow: hidden;
    background: var(--page);
  }
  .canvas {
    position: relative;
    width: 1200px;
    height: 1200px;
    background: var(--page);
  }
  .label {
    position: absolute;
    left: 200px;
    top: 100px;
    width: 800px;
    height: 1000px;
    background: var(--label-black);
    box-shadow: 18px 22px 30px rgba(0, 0, 0, 0.35);
    overflow: hidden;
    font-family: "Poiret One", sans-serif;
  }
  .label h1, .label h2, .label p { margin: 0; font-weight: 400; }
  .pattern-field {
    position: absolute;
    left: 0;
    right: 0;
    top: 390px;
    bottom: 0;
    background: linear-gradient(180deg,
      rgba(201, 154, 69, 0) 0%,
      rgba(201, 154, 69, 0.12) 35%,
      rgba(201, 154, 69, 0.22) 75%,
      rgba(201, 154, 69, 0.26) 100%);
  }
  .gold-band {
    position: absolute;
    left: 0;
    right: 0;
    height: 12px;
    background: linear-gradient(90deg, var(--gold-deep), var(--gold-light) 30%, var(--gold) 55%, var(--gold-light) 78%, var(--gold-deep));
  }
  .gold-band::after {
    content: "";
    position: absolute;
    left: 0;
    right: 0;
    top: 4px;
    height: 3px;
    background: rgba(0, 0, 0, 0.55);
  }
  .gold-band--top { top: 32px; }
  .gold-band--bottom { top: 872px; }
  .brand {
    position: absolute;
    top: 82px;
    left: 0;
    right: 0;
    display: flex;
    flex-direction: column;
    align-items: center;
    gap: 14px;
  }
  .brand-mark {
    width: 44px;
    height: 44px;
    border-radius: 50%;
    background: var(--gold);
  }
  .brand-name {
    color: var(--gold);
    font-size: 36px;
    letter-spacing: 6px;
    text-transform: uppercase;
  }
  .range-name {
    position: absolute;
    top: 312px;
    left: 0;
    right: 0;
    text-align: center;
    color: var(--gold-muted);
    font-size: 68px;
    line-height: 1.2;
    letter-spacing: 1px;
  }
  .title-lockup {
    position: absolute;
    top: 452px;
    left: 0;
    right: 0;
    text-align: center;
  }
  .title-word {
    position: relative;
    display: inline-block;
  }
  .varietal {
    color: var(--ivory);
    font-size: 170px;
    line-height: 1;
  }
  .vintage {
    position: absolute;
    top: 20px;
    left: 140px;
    color: var(--ivory);
    font-size: 34px;
    line-height: 1;
    letter-spacing: 1px;
  }
  .volume-info {
    position: absolute;
    top: 918px;
    left: 0;
    right: 0;
    text-align: center;
    color: var(--ivory);
    font-size: 25px;
    line-height: 1.2;
    font-style: italic;
    letter-spacing: 0.5px;
  }
</style>
</head>
<body>
<main class="canvas">
  <section class="label">
    <div class="pattern-field" role="img" aria-label="Gold art-deco pattern of nested diamond chevrons fading up from the label base"></div>
    <div class="gold-band gold-band--top"></div>

    <div class="brand">
      <span class="brand-mark"></span>
      <span class="brand-name">Southmere</span>
    </div>

    <h2 class="range-name">Gilded Crest</h2>

    <div class="title-lockup">
      <div class="title-word">
        <span class="vintage">2015</span>
        <h1 class="varietal">Shiraz</h1>
      </div>
    </div>

    <div class="gold-band gold-band--bottom"></div>
    <p class="volume-info">750 Ml. &nbsp;Alc. 12.5% By Volume</p>
  </section>
</main>
</body>
</html>
```